Velmora and Co Business Card Design

Looking for a business card design. Wanting Smart, Clean and Sharp looking to promote Velmora and Co, our Import Export Business - like Black, White and natural textures. I have uploaded our logo. I like a rounded font but open to other ideas
Being that we have a wide range of products on offer we are looking for a neutral yet eye catching card. We would also like to have Import - Export on the business card to be clear on want our business does.

Target Market(s)

Import export market

Industry/Entity Type

Importer

Contact Information for Business Card

Mr Tobias Kernwell
tobias.kernwell@velmoraandco.com.au
+61 (0) 417 630 284
www.velmoraandco.com.au

Font styles to use
Other font styles liked:
• Unsure of actual font name but something rounded and clean

Colors

Designer to choose colors to be used in the design.

Requirements
Must have
• Instagram icon
• Facebook icon

```html
<!DOCTYPE html>
<html lang="en">
<head>
<meta charset="utf-8">
<title>Velmora and Co Business Card</title>
<link href="https://fonts.googleapis.com/css2?family=Roboto+Condensed:wght@700&family=Roboto:wght@400&family=Montserrat:wght@500&display=swap" rel="stylesheet">
<style>
  :root {
    --ink: #1c1a1a;
    --paper: #ffffff;
    --backdrop: #2b2c30;
    --rule: #3a3a3a;
  }
  * { margin: 0; padding: 0; box-sizing: border-box; }
  html, body { width: 1200px; height: 800px; overflow: hidden; }
  body {
    background: var(--backdrop);
    display: flex;
    align-items: center;
    justify-content: center;
    gap: 40px;
  }
  .card {
    position: relative;
    width: 540px;
    height: 309px;
    background: var(--paper);
    color: var(--ink);
  }
  /* Front */
  .card-front .frame {
    position: absolute;
    inset: 14px;
    border: 1.5px solid var(--ink);
  }
  .brand {
    display: flex;
    align-items: center;
    gap: 10px;
    font-family: "Roboto Condensed", sans-serif;
    font-weight: 700;
    text-transform: uppercase;
    color: var(--ink);
    white-space: nowrap;
  }
  .brand-square { background: var(--ink); flex: none; }
  .card-front .brand {
    position: absolute;
    left: 50%;
    top: 98px;
    transform: translateX(-50%);
    font-size: 26px;
    letter-spacing: 1px;
  }
  .card-front .brand-square { width: 30px; height: 30px; }
  .tagline {
    font-family: "Montserrat", sans-serif;
    font-weight: 500;
    text-transform: uppercase;
    letter-spacing: 3px;
    color: var(--ink);
    white-space: nowrap;
  }
  .card-front .tagline {
    position: absolute;
    left: 0; right: 0;
    top: 146px;
    text-align: center;
    font-size: 10px;
  }
  .front-url {
    position: absolute;
    left: 0; right: 0;
    top: 196px;
    text-align: center;
    font-family: "Montserrat", sans-serif;
    font-weight: 500;
    font-size: 11px;
    letter-spacing: 3.5px;
    text-transform: uppercase;
  }
  /* Back */
  .back-brand-block {
    position: absolute;
    right: 40px;
    top: 40px;
    display: flex;
    flex-direction: column;
    align-items: flex-end;
    gap: 6px;
  }
  .card-back .brand { font-size: 20px; letter-spacing: 0.5px; }
  .card-back .brand-square { width: 24px; height: 24px; }
  .card-back .tagline { font-size: 8.5px; letter-spacing: 2.5px; }
  .holder {
    position: absolute;
    left: 30px;
    top: 110px;
    display: flex;
    align-items: center;
    width: 480px;
    gap: 10px;
  }
  .holder-name {
    font-family: "Roboto Condensed", sans-serif;
    font-weight: 700;
    font-size: 17px;
    text-transform: uppercase;
    white-space: nowrap;
  }
  .holder-rule { flex: 1; height: 1px; background: var(--rule); }
  .contact-list {
    position: absolute;
    right: 30px;
    top: 130px;
    list-style: none;
    font-family: "Roboto", sans-serif;
    font-size: 12.5px;
    line-height: 21px;
  }
  .contact-item {
    display: flex;
    align-items: center;
    justify-content: flex-end;
    gap: 8px;
  }
  .contact-icon {
    width: 15px; height: 15px;
    background: var(--ink);
    display: flex;
    align-items: center;
    justify-content: center;
  }
  .social {
    position: absolute;
    left: 30px;
    bottom: 28px;
    display: flex;
    align-items: center;
    gap: 8px;
  }
  .social-square { width: 18px; height: 18px; background: var(--ink); }
  .social-handle {
    font-family: "Roboto", sans-serif;
    font-size: 12.5px;
    color: var(--ink);
    margin-left: 2px;
  }
</style>
</head>
<body>
  <section class="card card-front">
    <div class="frame"></div>
    <div class="brand"><span class="brand-square"></span>Velmora and Co</div>
    <p class="tagline">Import - Export</p>
    <p class="front-url">www.velmoraandco.com.au</p>
  </section>

  <section class="card card-back">
    <div class="back-brand-block">
      <div class="brand"><span class="brand-square"></span>Velmora and Co</div>
      <p class="tagline">Import - Export</p>
    </div>
    <div class="holder">
      <span class="holder-name">Mr Tobias Kernwell</span>
      <span class="holder-rule"></span>
    </div>
    <ul class="contact-list">
      <li class="contact-item">+61 (0) 417 630 284
        <span class="contact-icon"><svg width="9" height="9" viewBox="0 0 10 10"><path d="M2 1 L4 1 L4.6 3 L3.4 3.8 Q4.4 5.8 6.2 6.6 L7 5.4 L9 6 L9 8 Q9 9 8 9 Q1 8.5 1 2 Q1 1 2 1Z" fill="#fff"/></svg></span>
      </li>
      <li class="contact-item">tobias.kernwell@velmoraandco.com.au
        <span class="contact-icon"><svg width="10" height="8" viewBox="0 0 10 8"><rect x="0.5" y="0.5" width="9" height="7" fill="none" stroke="#fff"/><path d="M0.5 0.5 L5 4.5 L9.5 0.5" fill="none" stroke="#fff"/></svg></span>
      </li>
      <li class="contact-item">www.velmoraandco.com.au
        <span class="contact-icon"><svg width="10" height="10" viewBox="0 0 10 10"><circle cx="5" cy="5" r="4.3" fill="none" stroke="#fff"/><ellipse cx="5" cy="5" rx="1.8" ry="4.3" fill="none" stroke="#fff"/><path d="M0.7 5 H9.3" stroke="#fff"/></svg></span>
      </li>
    </ul>
    <div class="social" aria-label="Social profiles">
      <span class="social-square" aria-hidden="true"></span>
      <span class="social-square" aria-hidden="true"></span>
      <span class="social-handle">@velmoraandco</span>
    </div>
  </section>
</body>
</html>
```